Startup online payment business - Sporting / Golf, Swift Tee payment

Background:
Our business name is "Swift Tee" we provide online payments for golfing services via our website. We currently have a logo used on our website. No other design style has been developed. Our aim is to remove cash payments for service at golf clubs.

Our Key Values:
Quick and easy
Formal and polite
Fun with professional boundary
Mate-ship relationships
100% online digital

What we want from you:
Marketing design to be used on posters and stickers in a retail setting to direct customers to our online payment Chanel.
Design must incorporate attached logo, URL swifttee.com.au and our key values can act as a guide the type of design. We have used color Hex#007672 for logo background. We are open to use other colors.

Target Market(s)

Golf clubs and golf players

Industry/Entity Type

Golf Course

Font styles to use
Sans Serif

Requirements
Must have
• Directions to online payment via URL: swifttee.com.au
Nice to have
• We like the idea of the slogan: No Cash - No worries. Have attached home screen that will be available from URL link. Consideration if using mobile phone in image. Push the online payment and steps 1. Visit swifttee.com 2. Select club 3. Confirm payment
Should not have
• Cartoons

```html
<!DOCTYPE html>
<html lang="en">
<head>
<meta charset="utf-8">
<title>Swift Tee – No Cash-No Worries</title>
<link href="https://fonts.googleapis.com/css2?family=Poppins:wght@500;600;700;800&family=Roboto:ital,wght@0,400;1,400&display=swap" rel="stylesheet">
<style>
  :root {
    --brand-teal: #007672;
    --ink-grey: #3a3a3a;
    --bg-top: #ffffff;
    --bg-bottom: #ecece9;
    --white: #ffffff;
    --pill-start: #00a872;
    --pill-end: #00b2dc;
  }
  html, body {
    margin: 0;
    padding: 0;
    overflow: hidden;
  }
  .poster {
    position: relative;
    width: 1200px;
    height: 677px;
    overflow: hidden;
    background: linear-gradient(180deg, var(--bg-top) 0%, var(--bg-top) 40%, var(--bg-bottom) 100%);
    font-family: "Poppins", sans-serif;
    color: var(--brand-teal);
  }
  .brand-block {
    position: absolute;
    left: 44px;
    top: 0;
    width: 209px;
    height: 166px;
    background: var(--brand-teal);
    display: flex;
    align-items: center;
    justify-content: center;
  }
  .brand-name {
    font-family: "Poppins", sans-serif;
    font-weight: 600;
    font-size: 30px;
    color: var(--white);
    letter-spacing: 1px;
  }
  .headline {
    position: absolute;
    left: 330px;
    width: 712px;
    top: 102px;
    margin: 0;
    text-align: center;
    font-weight: 700;
    font-size: 62px;
    line-height: 1;
    letter-spacing: -0.5px;
  }
  .values-title {
    position: absolute;
    left: 430px;
    width: 334px;
    top: 244px;
    margin: 0;
    text-align: center;
    font-weight: 800;
    font-size: 33px;
    line-height: 1;
  }
  .values-art {
    position: absolute;
    left: 0;
    top: 0;
    width: 1200px;
    height: 677px;
  }
  .value-label {
    position: absolute;
    width: 150px;
    margin-left: -75px;
    text-align: center;
    font-weight: 800;
    font-size: 16px;
    line-height: 1.05;
    text-transform: uppercase;
    transform: translateY(-50%);
  }
  .payment-direction {
    position: absolute;
    left: 898px;
    width: 280px;
    top: 588px;
    margin: 0;
    text-align: center;
    font-family: "Roboto", sans-serif;
    font-style: italic;
    font-size: 16px;
    color: var(--ink-grey);
  }
  .payment-url {
    position: absolute;
    left: 898px;
    top: 613px;
    width: 280px;
    height: 43px;
    border-radius: 22px;
    background: linear-gradient(90deg, var(--pill-start), var(--pill-end));
    color: var(--white);
    font-family: "Roboto", sans-serif;
    font-size: 26px;
    line-height: 43px;
    text-align: center;
  }
</style>
</head>
<body>
<main class="poster">
  <div class="brand-block"><span class="brand-name">Swift Tee</span></div>

  <h1 class="headline">No Cash-No Worries</h1>
  <h2 class="values-title">OUR KEY VALUES:</h2>

  <svg class="values-art" viewBox="0 0 1400 790" aria-hidden="true">
    <defs>
      <linearGradient id="ring-grey" x1="0" y1="0" x2="0" y2="1">
        <stop offset="0" stop-color="#f0f0f0"/>
        <stop offset="1" stop-color="#cfcfcf"/>
      </linearGradient>
      <linearGradient id="arc-one" gradientUnits="userSpaceOnUse" x1="123" y1="0" x2="353" y2="0">
        <stop offset="0" stop-color="#1aa3bd"/>
        <stop offset="1" stop-color="#00c49e"/>
      </linearGradient>
      <linearGradient id="arc-two" gradientUnits="userSpaceOnUse" x1="345" y1="0" x2="575" y2="0">
        <stop offset="0" stop-color="#12c395"/>
        <stop offset="1" stop-color="#00d58a"/>
      </linearGradient>
      <linearGradient id="arc-three" gradientUnits="userSpaceOnUse" x1="566" y1="0" x2="796" y2="0">
        <stop offset="0" stop-color="#38cc6a"/>
        <stop offset="1" stop-color="#8fcd37"/>
      </linearGradient>
      <linearGradient id="arc-four" gradientUnits="userSpaceOnUse" x1="790" y1="0" x2="1020" y2="0">
        <stop offset="0" stop-color="#9ccf3a"/>
        <stop offset="1" stop-color="#f6be18"/>
      </linearGradient>
      <linearGradient id="arc-five" gradientUnits="userSpaceOnUse" x1="1013" y1="0" x2="1243" y2="0">
        <stop offset="0" stop-color="#f7a51f"/>
        <stop offset="1" stop-color="#ff3d5b"/>
      </linearGradient>
      <filter id="soft-shadow" x="-20%" y="-20%" width="140%" height="140%">
        <feDropShadow dx="0" dy="3" stdDeviation="4" flood-color="#000" flood-opacity="0.12"/>
      </filter>
    </defs>

    <g class="value-rings">
      <circle cx="238" cy="500" r="88" fill="url(#ring-grey)"/>
      <circle cx="238" cy="500" r="78" fill="#fff" filter="url(#soft-shadow)"/>
      <circle cx="460" cy="460" r="88" fill="url(#ring-grey)"/>
      <circle cx="460" cy="460" r="78" fill="#fff" filter="url(#soft-shadow)"/>
      <circle cx="681" cy="500" r="88" fill="url(#ring-grey)"/>
      <circle cx="681" cy="500" r="78" fill="#fff" filter="url(#soft-shadow)"/>
      <circle cx="905" cy="460" r="88" fill="url(#ring-grey)"/>
      <circle cx="905" cy="460" r="78" fill="#fff" filter="url(#soft-shadow)"/>
      <circle cx="1128" cy="500" r="88" fill="url(#ring-grey)"/>
      <circle cx="1128" cy="500" r="78" fill="#fff" filter="url(#soft-shadow)"/>
    </g>

    <g class="value-arcs" fill="none" stroke-width="10" stroke-linecap="round">
      <path d="M123 500 A115 115 0 0 0 353 500" stroke="url(#arc-one)"/>
      <path d="M345 460 A115 115 0 0 1 575 460" stroke="url(#arc-two)"/>
      <path d="M566 500 A115 115 0 0 0 796 500" stroke="url(#arc-three)"/>
      <path d="M790 460 A115 115 0 0 1 1020 460" stroke="url(#arc-four)"/>
      <path d="M1013 500 A115 115 0 0 0 1243 500" stroke="url(#arc-five)"/>
    </g>
  </svg>

  <p class="value-label" style="left:204px; top:423px;">Quick<br>and<br>easy</p>
  <p class="value-label" style="left:394px; top:394px;">Formal<br>and<br>polite</p>
  <p class="value-label" style="left:584px; top:449px;">Fun with<br>professional<br>boundary</p>
  <p class="value-label" style="left:776px; top:394px;">Mate-ship<br>relationships</p>
  <p class="value-label" style="left:967px; top:423px;">100%<br>online<br>digital</p>

  <p class="payment-direction">Directions to online payment</p>
  <div class="payment-url">swifttee.com.au</div>
</main>
</body>
</html>
```